Relaydock Tech Company Website B2B Dev Teams Corvane

We need a completely new website for this tech company. We offer software as a service to companies that have private Corvane software. Our clients are developers, tech teams, and companies (B2B). We offer a way to keep Corvane devices updated worldwide without needing a Mirath Shelf account, which suits corporate-owned single-use devices very well.
Our public is technicians (software developers), not people who use smartphones. Most clients run Relaydock on tablets, drones, point-of-sale devices, etc.
The most used feature is the background update, which requires no user interaction. Our product helps developers keep their private enterprise applications updated. Some references of what developers like to see:
dovetra.com, namboret.com, wavolith.com, temiqo.io, kelbru.io
The green doesn't suit it very well. Feel free to change the logo's color (source images .ai .psd attached). The current website has only five small pages. The new one can have five at most (it can have less). The images of the "update strategies" aren't good. It can be replaced by "mock-like" images mimicking how Corvane interacts with the user. The proportion of the tool icons isn't good. The login and signup forms can be improved a lot.
We hope for a modern website for a tech company with new colors that, at first glance, convey a sense of quality. We want the current standard for SaaS (software as a service) providers' websites.
https://www.relaydock-example.com/
NO WORDPRESS.
We want it built using Next, Nuxt, or another good static build tool.

Target Market(s)
Corvane Software Development
Industry/Entity Type
Software
Coding
Coded - Design and coding required
Number of Pages Required
4 page
Requirements
Must have
- We want it built using Next, Nuxt, or another good static build tool

Nice to have
- Corvane message notification mockups instead screenshots

Should not have
- wordpress

```html
<!DOCTYPE html>
<html lang="en">
<head>
<meta charset="utf-8">
<title>Relaydock — Corvane Enterprise App Management</title>
<link href="https://fonts.googleapis.com/css2?family=Poppins:wght@400;500;600;700;800&display=swap" rel="stylesheet">
<style>
:root{
  --ink:#16141d;
  --ink-2:#1f1c29;
  --ink-line:#2d2a38;
  --paper:#f4f4f6;
  --white:#ffffff;
  --purple:#7b3cf0;
  --purple-2:#9b5cff;
  --text:#1c1a24;
  --muted:#7c7a86;
  --muted-light:#b9b7c4;
  --mint:#dff3ea;
  --green:#2f9b6a;
  --green-soft:#3fb57d;
  --red:#e0504a;
  --rule:#e6e7eb;
}
*{box-sizing:border-box;margin:0;padding:0}
html,body{width:1200px;height:3592px;overflow:hidden}
body{font-family:"Poppins",sans-serif;background:var(--paper);color:var(--text);position:relative}
a{color:inherit;text-decoration:none}
.btn{display:inline-flex;align-items:center;justify-content:center;height:42px;padding:0 22px;border-radius:21px;font-size:12px;font-weight:600;letter-spacing:.4px;white-space:nowrap}
.btn-primary{background:linear-gradient(90deg,var(--purple),var(--purple-2));color:var(--white)}
.btn-ghost{border:1.5px solid var(--white);color:var(--white)}
.btn-outline{border:1.5px solid var(--text);color:var(--text);background:var(--white)}
.brand{font-weight:800;color:var(--purple-2);letter-spacing:-1px}

/* shared mock UI */
.ui{position:absolute;overflow:hidden;font-size:8px;color:var(--text);background:var(--white)}
.ui-bar{height:24px;background:var(--ink);display:flex;align-items:center;gap:16px;padding:0 12px;color:var(--muted-light);font-size:7px}
.ui-bar b{color:var(--purple-2);font-size:10px;font-weight:800}
.ui-bar .sel{color:var(--white)}
.ui-bar .go{margin-left:auto;background:var(--purple);color:#fff;padding:3px 10px;border-radius:3px}
.ui-body{padding:14px 18px;background:linear-gradient(180deg,var(--mint) 0,#fff 130px)}
.ui-cards{display:flex;gap:10px}
.ui-done{width:200px;height:78px;border-radius:6px;background:var(--green);color:#fff;padding:12px;font-weight:600;font-size:9px}
.ui-done small{display:block;font-weight:400;opacity:.8;margin-top:4px;font-size:7px}
.ui-stat{width:118px;height:78px;border-radius:6px;background:#fff;border:1px solid var(--rule);padding:10px}
.ui-stat strong{display:block;font-size:22px;font-weight:600;line-height:26px}
.ui-stat span{color:var(--muted);font-size:7px}
.ui-stat i{display:block;height:4px;border-radius:2px;margin-top:8px;background:linear-gradient(90deg,var(--green-soft) var(--p),var(--rule) var(--p))}
.ui-h{font-size:11px;font-weight:600;margin:16px 0 6px;display:flex;justify-content:space-between}
.ui-h em{font-style:normal;font-weight:400;color:var(--muted);font-size:7px}
.ui table{width:100%;border-collapse:collapse}
.ui th{background:#f1f2f4;text-align:left;font-weight:600;padding:5px 6px;font-size:7px}
.ui td{padding:4px 6px;border-bottom:1px solid var(--rule);font-size:7px;color:#4a4852;white-space:nowrap}
.chip{display:inline-block;padding:1px 6px;border-radius:3px;background:var(--green-soft);color:#fff;font-size:6.5px}
.chip.off{background:var(--red)}
.dot{display:inline-block;width:7px;height:7px;border-radius:2px;background:var(--purple-2)}

/* hero */
.hero{position:absolute;left:0;top:0;width:1200px;height:1100px;background:
  radial-gradient(ellipse 700px 260px at 600px 380px,rgba(123,60,240,.18),transparent 70%),var(--ink);overflow:hidden}
.topbar{position:absolute;left:0;top:28px;width:1200px;height:60px}
.topbar .brand{position:absolute;left:86px;top:8px;font-size:38px}
.nav-pill{position:absolute;left:392px;top:10px;height:44px;width:420px;border-radius:22px;background:var(--ink-2);display:flex;align-items:center;padding:0 6px;gap:4px}
.nav-pill a{font-size:11px;font-weight:600;color:var(--muted-light);padding:9px 14px;border-radius:16px;letter-spacing:.4px}
.nav-pill a.active{background:var(--white);color:var(--text)}
.topbar .auth{position:absolute;right:86px;top:12px;display:flex;gap:14px}
.topbar .auth .btn{height:38px;padding:0 18px;font-size:11px}
.hero h1{position:absolute;left:0;top:154px;width:1200px;text-align:center;color:var(--white);font-size:56px;line-height:70px;font-weight:700;letter-spacing:-.5px}
.hero h1 .mark{display:inline-block;width:34px;height:34px;border-radius:6px;background:#7fd05a;vertical-align:middle;margin:0 8px 8px}
.hero .lead{position:absolute;left:0;top:320px;width:1200px;text-align:center;color:var(--muted-light);font-size:16px}
.hero .cta{position:absolute;left:517px;top:388px;width:166px}
.hero-shot{left:192px;top:496px;width:816px;height:416px;border-radius:8px;box-shadow:0 30px 60px rgba(0,0,0,.35)}
.swoosh{position:absolute;right:-40px;top:620px;width:380px;height:240px}
.toolchain{position:absolute;left:150px;top:998px;width:900px;display:flex;justify-content:space-between;align-items:center}
.tool{display:flex;align-items:center;gap:10px;color:var(--muted-light);font-size:20px;font-weight:500}
.tool i{width:22px;height:22px;border-radius:50%;background:var(--muted-light);display:block}

/* quick usage */
.section-title{font-size:40px;font-weight:600;color:var(--text)}
.quick{position:absolute;left:0;top:1160px;width:1200px}
.quick .section-title{text-align:center}
.quick-cards{position:absolute;left:144px;top:92px;display:flex;gap:20px}
.quick-card{width:292px;height:134px;background:var(--white);border-radius:14px;box-shadow:0 10px 30px rgba(40,30,80,.08);display:flex;align-items:center;gap:22px;padding:0 26px}
.quick-card .ico{width:66px;height:66px;border-radius:14px;background:linear-gradient(135deg,var(--purple),var(--purple-2));display:flex;align-items:center;justify-content:center;flex:none}
.quick-card h3{font-size:22px;font-weight:500}
.quick-card p{font-size:11px;color:var(--muted);margin-top:2px}

/* features */
.features{position:absolute;left:0;top:1480px;width:1200px;height:560px}
.features .section-title{position:absolute;left:88px;top:14px}
.feature-list{position:absolute;left:88px;top:92px;width:500px}
.feature{display:flex;gap:22px;padding:18px 22px;border-radius:12px;margin-bottom:14px;width:490px}
.feature .fi{width:44px;height:44px;flex:none;display:flex;align-items:center;justify-content:center}
.feature h4{font-size:17px;font-weight:500}
.feature p{font-size:11.5px;color:var(--muted);line-height:17px;margin-top:4px;width:300px}
.feature .arrow{margin-left:auto;align-self:center}
.feature.current{background:var(--ink);color:var(--white)}
.feature.current p{color:var(--muted-light)}
.feature-actions{position:absolute;left:88px;top:456px;display:flex;gap:14px}
.feature-actions .btn{width:164px}
.features-shot{left:664px;top:16px;width:536px;height:500px;border-radius:8px 0 0 8px;box-shadow:0 20px 50px rgba(40,30,80,.15)}
.features-shot .ui-done{width:150px;height:64px}
.features-shot .ui-stat{width:96px;height:64px}
.features-shot .ui-stat strong{font-size:17px;line-height:20px}
.features-shot td,.features-shot th{padding:4px 4px;font-size:6.5px}

/* update strategies */
.strategies{position:absolute;left:0;top:2080px;width:1200px;height:700px}
.strategies .section-title{text-align:center;position:absolute;left:0;top:20px;width:1200px}
.strategies .band{position:absolute;left:-40px;top:190px;width:1280px;height:300px}
.phones{position:absolute;left:180px;top:112px;display:flex;gap:50px}
.phone{width:172px;text-align:center}
.phone .device{position:relative;width:172px;height:476px;border-radius:24px;background:#111014;padding:8px;box-shadow:0 16px 30px rgba(0,0,0,.25)}
.screen{position:relative;width:156px;height:460px;border-radius:18px;overflow:hidden;background:#2c2b31;color:#fff;text-align:left}
.sbar{height:18px;display:flex;justify-content:space-between;padding:4px 12px;font-size:7px;color:#ddd}
.navbar{position:absolute;left:0;bottom:0;width:156px;height:26px;display:flex;justify-content:space-around;align-items:center}
.navbar i{width:8px;height:8px;border:1.5px solid #bbb;border-radius:2px}
.navbar i:nth-child(2){border-radius:50%}
.wall{position:absolute;left:0;top:0;width:156px;height:460px;background:linear-gradient(180deg,#5a6a73 0%,#3b3f3a 55%,#1e1f1d 100%)}
.lock-time{position:absolute;top:58px;width:156px;text-align:center;font-size:40px;font-weight:300}
.lock-date{position:absolute;top:110px;width:156px;text-align:center;font-size:8px;color:#e6e6e6}
.notice{position:absolute;left:10px;top:150px;width:136px;background:rgba(255,255,255,.92);color:var(--text);border-radius:8px;padding:8px;font-size:7px;line-height:10px}
.notice b{display:block;font-size:7.5px}
.dialog{position:absolute;left:12px;top:150px;width:132px;background:#fff;color:var(--text);border-radius:6px;padding:10px;font-size:7px;line-height:10px}
.dialog b{display:block;font-size:8px;margin-bottom:4px}
.dialog .acts{display:flex;justify-content:flex-end;gap:10px;margin-top:10px;color:var(--purple);font-weight:600}
.magic{position:absolute;left:38px;top:170px;width:80px;height:80px;border-radius:10px;background:radial-gradient(circle,#6e6c78 0,#3a3942 70%)}
.phone > span{display:block;margin-top:38px;font-size:19px;font-weight:500;white-space:nowrap}

/* host */
.host{position:absolute;left:0;top:2780px;width:1200px;height:520px}
.host-shot{left:88px;top:66px;width:572px;height:428px;border-radius:10px;box-shadow:0 20px 50px rgba(40,30,80,.15);z-index:2}
.host-head{height:70px;background:var(--ink);display:flex;justify-content:space-between;align-items:center;padding:0 22px;color:var(--muted-light);font-size:8px}
.host-head b{color:var(--purple-2);font-size:20px;font-weight:800;letter-spacing:-.5px}
.host-body{padding:16px 22px}
.host-card{border:1px solid var(--rule);border-radius:6px;padding:12px;margin-bottom:12px}
.host-card .ok{display:flex;align-items:center;gap:10px;background:var(--mint);border-radius:4px;padding:8px;font-size:10px;font-weight:600;color:var(--green)}
.bar{height:7px;border-radius:4px;background:var(--rule);margin-top:8px;overflow:hidden}
.bar i{display:block;height:7px;background:var(--green-soft)}
.nums{display:flex;gap:40px;margin-top:8px}
.nums strong{display:block;font-size:14px;font-weight:600}
.nums span{font-size:7px;color:var(--muted)}
.host h2{position:absolute;left:740px;top:36px;font-size:36px;line-height:44px;font-weight:600;width:400px}
.host p{position:absolute;left:740px;top:172px;font-size:15px;color:var(--muted);width:340px;line-height:22px}
.host .actions{position:absolute;left:740px;top:244px;display:flex;gap:12px}
.host .actions .btn{height:40px;font-size:11px;padding:0 20px}

/* footer */
.site-footer{position:absolute;left:0;top:3300px;width:1200px;height:292px;background:var(--ink);color:var(--white)}
.site-footer .brand{position:absolute;left:0;top:52px;width:1200px;text-align:center;font-size:76px;line-height:90px}
.foot-nav{position:absolute;left:0;top:156px;width:1200px;display:flex;justify-content:center;gap:34px;font-size:12px;font-weight:600;color:var(--muted-light)}
.to-top{position:absolute;left:1090px;top:100px;width:40px;height:40px;border-radius:50%;background:var(--purple);display:flex;align-items:center;justify-content:center}
.foot-rule{position:absolute;left:88px;top:218px;width:1024px;height:1px;background:var(--ink-line)}
.foot-base{position:absolute;left:88px;top:246px;width:1024px;font-size:12px;color:var(--muted-light)}
.foot-base .copy{text-align:center}
.foot-base .legal{position:absolute;right:0;top:0;display:flex;gap:10px}
</style>
</head>
<body>

<header class="hero">
  <div class="topbar">
    <a class="brand" href="https://www.relaydock-example.com/">relaydock</a>
    <nav class="nav-pill">
      <a class="active" href="#">HOME</a><a href="#">FEATURES</a><a href="#">PRICING</a><a href="#">DOCS</a><a href="#">STATUS</a>
    </nav>
    <div class="auth">
      <a class="btn btn-ghost" href="#">SIGN UP FREE</a>
      <a class="btn btn-primary" href="#">SIGN IN</a>
    </div>
  </div>
  <h1>Corvane<span class="mark"></span>Enterprise App<br>Management Made Easy</h1>
  <p class="lead">Keep your private Corvane application self-updated without any third-party process.</p>
  <a class="btn btn-primary cta" href="#">SIGN UP FREE</a>
  <svg class="swoosh" viewBox="0 0 380 240" aria-hidden="true">
    <path d="M0 60 C120 20 260 80 380 200" stroke="#5b3aa0" stroke-width="26" fill="none" opacity=".55" stroke-linecap="round"/>
  </svg>

  <div class="ui hero-shot">
    <div class="ui-bar"><b>relaydock</b><span class="sel">Field App v4.2</span><span>Devices</span><span>Versions</span><span>Reports</span><span class="go">Upload APK</span></div>
    <div class="ui-body">
      <div class="ui-cards">
        <div class="ui-done">All updates done<small>Every enrolled device runs the latest version</small></div>
        <div class="ui-stat"><strong>76</strong><span>Installed devices</span><i style="--p:80%"></i></div>
        <div class="ui-stat"><strong>52</strong><span>Updated this week</span><i style="--p:65%"></i></div>
        <div class="ui-stat"><strong>24</strong><span>Pending restarts</span><i style="--p:30%"></i></div>
      </div>
      <div class="ui-h">Reviews <em>Last 30 days</em></div>
      <table>
        <tr><th>Date</th><th>Version</th><th>Status</th><th>Message</th><th></th></tr>
        <tr><td>12.11.2021</td><td>4.2.0</td><td><span class="chip">Done</span></td><td>Background install finished on kiosk units</td><td><span class="dot"></span></td></tr>
        <tr><td>11.11.2021</td><td>4.1.9</td><td><span class="chip">Done</span></td><td>Rollout completed for warehouse tablets</td><td><span class="dot"></span></td></tr>
        <tr><td>10.11.2021</td><td>4.1.9</td><td><span class="chip">Done</span></td><td>Forced update accepted by all devices</td><td><span class="dot"></span></td></tr>
        <tr><td>09.11.2021</td><td>4.1.8</td><td><span class="chip off">Error</span></td><td>Signature mismatch on two handheld units</td><td><span class="dot"></span></td></tr>
        <tr><td>08.11.2021</td><td>4.1.8</td><td><span class="chip">Done</span></td><td>New version uploaded and enabled</td><td><span class="dot"></span></td></tr>
        <tr><td>07.11.2021</td><td>4.1.7</td><td><span class="chip">Done</span></td><td>Status bar notice shown to users</td><td><span class="dot"></span></td></tr>
        <tr><td>06.11.2021</td><td>4.1.7</td><td><span class="chip">Done</span></td><td>Device enrollment batch added</td><td><span class="dot"></span></td></tr>
        <tr><td>05.11.2021</td><td>4.1.6</td><td><span class="chip">Done</span></td><td>Exception report cleared</td><td><span class="dot"></span></td></tr>
      </table>
    </div>
  </div>

  <div class="toolchain">
    <span class="tool"><i></i>Lunaport</span>
    <span class="tool"><i></i>Fluvex</span>
    <span class="tool"><i></i>Brindle</span>
    <span class="tool"><i></i>Orvisoft</span>
    <span class="tool"><i></i>Kinetra Native</span>
  </div>
</header>

<section class="quick">
  <h2 class="section-title">Quick Usage</h2>
  <div class="quick-cards">
    <div class="quick-card">
      <div class="ico"><svg width="30" height="30" viewBox="0 0 24 24" fill="none" stroke="#fff" stroke-width="2" stroke-linecap="round"><circle cx="12" cy="12" r="10"/><path d="M12 7v9M8 12l4 4 4-4"/></svg></div>
      <div><h3>Download</h3><p>relaydock-release.aar</p></div>
    </div>
    <div class="quick-card">
      <div class="ico"><svg width="30" height="30" viewBox="0 0 24 24" fill="none" stroke="#fff" stroke-width="2"><circle cx="12" cy="12" r="3"/><path d="M12 2v3M12 19v3M2 12h3M19 12h3M4.9 4.9l2.1 2.1M17 17l2.1 2.1M4.9 19.1L7 17M17 7l2.1-2.1"/></svg></div>
      <div><h3>Configure</h3><p>Set your API key</p></div>
    </div>
    <div class="quick-card">
      <div class="ico"><svg width="30" height="30" viewBox="0 0 24 24" fill="none" stroke="#fff" stroke-width="2" stroke-linejoin="round"><path d="M5 3h4l2 5-2.5 1.5a11 11 0 005 5L15 12l5 2v4a2 2 0 01-2 2A16 16 0 013 5a2 2 0 012-2z"/></svg></div>
      <div><h3>Call</h3><p>Relaydock.start()</p></div>
    </div>
  </div>
</section>

<section class="features">
  <h2 class="section-title">Features</h2>
  <div class="feature-list">
    <div class="feature">
      <div class="fi"><svg width="36" height="36" viewBox="0 0 24 24" fill="none" stroke="#1c1a24" stroke-width="1.5"><path d="M6 2h9l4 4v16H6z"/><path d="M15 2v4h4M9 12h7M9 16h7"/></svg></div>
      <div><h4>Host your apk</h4><p>Relaydock hosts your APK encrypted and uses versioned access. All the traffic is secured.</p></div>
      <svg class="arrow" width="22" height="22" viewBox="0 0 24 24" fill="none" stroke="#1c1a24" stroke-width="2"><path d="M4 12h15M13 6l6 6-6 6"/></svg>
    </div>
    <div class="feature current">
      <div class="fi"><svg width="36" height="36" viewBox="0 0 24 24" fill="none" stroke="#fff" stroke-width="1.5"><rect x="3" y="4" width="18" height="12" rx="1"/><path d="M8 20h8M12 16v4"/></svg></div>
      <div><h4>Devices Enrollment</h4><p>Simple but effective ways to install your application for the first time on your devices.</p></div>
      <svg class="arrow" width="22" height="22" viewBox="0 0 24 24" fill="none" stroke="#fff" stroke-width="2"><path d="M4 12h15M13 6l6 6-6 6"/></svg>
    </div>
    <div class="feature">
      <div class="fi"><svg width="36" height="36" viewBox="0 0 24 24" fill="none" stroke="#1c1a24" stroke-width="1.5"><rect x="3" y="3" width="18" height="18" rx="2"/><path d="M8 8l-3 4 3 4M16 8l3 4-3 4"/></svg></div>
      <div><h4>Manage Versions</h4><p>Choose the application version running on the devices after uploading an APK.</p></div>
      <svg class="arrow" width="22" height="22" viewBox="0 0 24 24" fill="none" stroke="#1c1a24" stroke-width="2"><path d="M4 12h15M13 6l6 6-6 6"/></svg>
    </div>
  </div>
  <div class="feature-actions">
    <a class="btn btn-primary" href="#">SEE PRICING</a>
    <a class="btn btn-outline" href="#">SIGN UP FREE</a>
  </div>

  <div class="ui features-shot">
    <div class="ui-bar"><b>relaydock</b><span class="sel">Devices</span><span>Versions</span><span class="go">Add device</span></div>
    <div class="ui-body">
      <div class="ui-cards">
        <div class="ui-done">All updates done<small>76 of 76 devices current</small></div>
        <div class="ui-stat"><strong>76</strong><span>Installed</span><i style="--p:85%"></i></div>
        <div class="ui-stat"><strong>52</strong><span>Active today</span><i style="--p:60%"></i></div>
        <div class="ui-stat"><strong>3</strong><span>Exceptions</span><i style="--p:10%"></i></div>
      </div>
      <div class="ui-h">Installations <em>Sorted by last seen</em></div>
      <table>
        <tr><th>#</th><th>State</th><th>Device</th><th>Version</th><th>Last seen</th><th>Model</th></tr>
        <tr><td>1</td><td><span class="chip">On</span></td><td>POS-0142</td><td>4.2.0</td><td>2 min ago</td><td>T8 Tablet</td></tr>
        <tr><td>2</td><td><span class="chip">On</span></td><td>POS-0143</td><td>4.2.0</td><td>4 min ago</td><td>T8 Tablet</td></tr>
        <tr><td>3</td><td><span class="chip off">Off</span></td><td>DRN-0007</td><td>4.1.9</td><td>3 h ago</td><td>Flight unit</td></tr>
        <tr><td>4</td><td><span class="chip">On</span></td><td>KSK-0031</td><td>4.2.0</td><td>6 min ago</td><td>Kiosk 15</td></tr>
        <tr><td>5</td><td><span class="chip">On</span></td><td>KSK-0032</td><td>4.2.0</td><td>8 min ago</td><td>Kiosk 15</td></tr>
        <tr><td>6</td><td><span class="chip">On</span></td><td>HND-0210</td><td>4.2.0</td><td>11 min ago</td><td>Scanner X</td></tr>
        <tr><td>7</td><td><span class="chip off">Off</span></td><td>HND-0211</td><td>4.1.8</td><td>1 day ago</td><td>Scanner X</td></tr>
        <tr><td>8</td><td><span class="chip">On</span></td><td>POS-0150</td><td>4.2.0</td><td>15 min ago</td><td>T8 Tablet</td></tr>
        <tr><td>9</td><td><span class="chip">On</span></td><td>KSK-0040</td><td>4.2.0</td><td>19 min ago</td><td>Kiosk 15</td></tr>
        <tr><td>10</td><td><span class="chip">On</span></td><td>HND-0215</td><td>4.2.0</td><td>22 min ago</td><td>Scanner X</td></tr>
      </table>
    </div>
  </div>
</section>

<section class="strategies">
  <h2 class="section-title">Update Strategies</h2>
  <svg class="band" viewBox="0 0 1280 300" aria-hidden="true">
    <path d="M0 220 C300 60 700 40 1280 120" stroke="#b99cf2" stroke-width="40" fill="none" opacity=".45"/>
  </svg>
  <div class="phones">
    <div class="phone">
      <div class="device"><div class="screen">
        <div class="wall" role="img" aria-label="Lock screen wallpaper"></div>
        <div class="sbar" style="position:relative"><span>9:41</span><span>5G ▪▪▪</span></div>
        <div class="lock-time">1:50</div>
        <div class="lock-date">Friday, 12 November</div>
        <div class="notice"><b>Update available</b>Tap to install version 4.2.0</div>
        <div class="navbar"><i></i><i></i><i></i></div>
      </div></div>
      <span>Status Bar</span>
    </div>
    <div class="phone">
      <div class="device"><div class="screen">
        <div class="sbar"><span>9:41</span><span>5G ▪▪▪</span></div>
        <div class="dialog"><b>New version</b>A newer version of this app is ready to install.<div class="acts"><span>LATER</span><span>INSTALL</span></div></div>
        <div class="navbar"><i></i><i></i><i></i></div>
      </div></div>
      <span>Friendly Pop-up</span>
    </div>
    <div class="phone">
      <div class="device"><div class="screen">
        <div class="sbar"><span>9:41</span><span>5G ▪▪▪</span></div>
        <div class="dialog"><b>Update required</b>Install the new version to keep using this app.<div class="acts"><span>INSTALL</span></div></div>
        <div class="navbar"><i></i><i></i><i></i></div>
      </div></div>
      <span>Annoying Pop-up</span>
    </div>
    <div class="phone">
      <div class="device"><div class="screen">
        <div class="sbar"><span>9:41</span><span>5G ▪▪▪</span></div>
        <div class="magic" role="img" aria-label="Illustration of an update happening silently in the background"></div>
        <div class="navbar"><i></i><i></i><i></i></div>
      </div></div>
      <span>Background</span>
    </div>
  </div>
</section>

<section class="host">
  <div class="ui host-shot">
    <div class="host-head"><b>relaydock</b><span>Field App · Overview</span></div>
    <div class="host-body">
      <div class="host-card">
        <div class="ui-h" style="margin:0 0 8px">Updates <em>Last 30 days</em></div>
        <div class="ok"><svg width="14" height="14" viewBox="0 0 24 24" fill="none" stroke="#2f9b6a" stroke-width="3"><path d="M4 12l5 5L20 6"/></svg>All updates Completed</div>
        <div class="bar"><i style="width:96%"></i></div>
        <div class="bar"><i style="width:82%"></i></div>
        <div class="bar"><i style="width:64%"></i></div>
      </div>
      <div class="host-card">
        <div class="ui-h" style="margin:0">Overall Updates</div>
        <div class="nums"><div><strong>1,240</strong><span>Installs</span></div><div><strong>318</strong><span>Devices</span></div><div><strong>12</strong><span>Versions</span></div></div>
      </div>
      <div class="host-card">
        <div class="ui-h" style="margin:0">Status updates <em>Live</em></div>
        <div class="bar"><i style="width:72%;background:var(--purple-2)"></i></div>
      </div>
    </div>
  </div>
  <h2>Host your APK, Manage and Enforce Versions</h2>
  <p>Track exceptions and installations, integrate with our API and much more!</p>
  <div class="actions">
    <a class="btn btn-primary" href="#">SEE ALL FEATURES</a>
    <a class="btn btn-outline" href="#">SIGN UP FREE</a>
  </div>
</section>

<footer class="site-footer">
  <div class="brand">relaydock</div>
  <a class="to-top" href="#"><svg width="16" height="16" viewBox="0 0 24 24" fill="none" stroke="#fff" stroke-width="2.5"><path d="M12 19V5M6 11l6-6 6 6"/></svg></a>
  <nav class="foot-nav"><a href="#">FEATURES</a><a href="#">PRICING</a><a href="#">DOCS</a><a href="#">STATUS</a></nav>
  <div class="foot-rule"></div>
  <div class="foot-base">
    <p class="copy">© Copyright 2021 Relaydock All Rights Reserved.</p>
    <div class="legal"><a href="#">Privacy policy</a><span>|</span><a href="#">Terms of Service</a></div>
  </div>
</footer>

</body>
</html>
```